Design an Outstanding flyer for my company.

I need a flyer designed for our window tinting company based in Brisbane Queensland Australia. The flyer will be targeting Home tinting. We also do mobile car tinting. Something in regards to this could be incorporated into the flyer as well.
I want it to be 2 sided DL size. Black background.
It really needs to Pop, and be a real attention getter.
It needs to be easy to read.
I have provided a mock up with the info on it from our marketing company. It will need a spellcheck etc to make sure everything is correct.
Everything about it can be changed however you like.
I have also included the company logo.

Lets see what you've got!

Target Market(s)

Home Owners

Industry/Entity Type

Home Improvement

Font styles to use
Other font styles liked:
• Duan Penh

Requirements
Must have
• All the information on the mock up. Clear and easy to read.
• Must Stand Out!

```html
<!DOCTYPE html>
<html lang="en">
<head>
<meta charset="utf-8">
<title>BrightSun Window Tinting – DL Flyer</title>
<link href="https://fonts.googleapis.com/css2?family=Anton&family=Oswald:wght@500;600&family=Montserrat:wght@500;600;700&family=Roboto+Condensed:wght@500&display=swap" rel="stylesheet">
<style>
:root{
  --stage:#dcd8d1;
  --ink:#000;
  --paper:#050505;
  --white:#ffffff;
  --gold-hi:#ffe24a;
  --gold:#f7b500;
  --amber:#e87a00;
  --orange:#ff8a00;
  --red:#f11414;
  --silver-hi:#ffffff;
  --silver:#bdbdbd;
  --silver-lo:#7a7a7a;
}
*{box-sizing:border-box;margin:0;padding:0}
html,body{width:1200px;height:1200px;overflow:hidden}
body{background:var(--stage);position:relative;font-family:"Roboto Condensed",sans-serif}

.side-label{position:absolute;top:36px;width:468px;text-align:center;font-family:"Montserrat",sans-serif;font-weight:600;font-size:31px;letter-spacing:1px;color:#111}
.side-label--front{left:104px}
.side-label--back{left:630px}

.flyer{position:absolute;top:86px;width:468px;height:992px;background:var(--paper);overflow:hidden;color:var(--white)}
.flyer--front{left:104px}
.flyer--back{left:630px}
.abs{position:absolute}

.gold-text{background:linear-gradient(180deg,var(--gold-hi) 0%,var(--gold) 45%,var(--amber) 100%);-webkit-background-clip:text;background-clip:text;color:transparent}
.silver-text{background:linear-gradient(180deg,var(--silver-hi) 0%,#e6e6e6 40%,var(--silver-lo) 55%,#f2f2f2 100%);-webkit-background-clip:text;background-clip:text;color:transparent}

/* front headline */
.headline-stack{left:34px;top:28px;font-family:"Anton",sans-serif;font-size:84px;line-height:78px;letter-spacing:-1px}
.promo-tag{left:214px;width:220px;height:104px;background:linear-gradient(180deg,#ffffff 0%,#e9e9e9 55%,#c9c9c9 100%);color:#111;display:flex;align-items:center;justify-content:center}
.promo-tag::before,.promo-tag::after{content:"";position:absolute;width:0;height:0}
.promo-tag--uv{top:34px}
.promo-tag--uv::before{left:-14px;top:0;border-top:28px solid transparent;border-right:14px solid var(--orange)}
.promo-tag--uv::after{right:0;bottom:-22px;border-top:22px solid var(--orange);border-left:28px solid transparent}
.promo-tag--privacy{top:151px}
.promo-tag--privacy::before{right:0;top:-22px;border-bottom:22px solid var(--orange);border-left:28px solid transparent}
.promo-tag--privacy::after{left:-14px;bottom:0;border-bottom:28px solid transparent;border-right:14px solid var(--orange)}

.uv-claim{display:flex;align-items:center;gap:8px;font-family:"Anton",sans-serif}
.uv-claim__words{font-size:19px;line-height:22px;letter-spacing:0}
.uv-claim__figure{font-size:50px;line-height:1;letter-spacing:-1px}
.uv-claim__figure sup{font-size:24px;vertical-align:top;position:relative;top:2px}
.privacy-claim{font-family:"Anton",sans-serif;text-align:center}
.privacy-claim__small{font-size:24px;letter-spacing:6px;line-height:28px}
.privacy-claim__big{font-size:40px;line-height:44px;letter-spacing:.5px}

.save-money{font-family:"Anton",sans-serif;font-size:78px;line-height:1;letter-spacing:-1px}

/* reason lists */
.reasons{display:flex;gap:4px;left:0;width:468px}
.reasons__col{display:flex;flex-direction:column;gap:2px}
.reasons__col--left{width:240px}
.reasons__col--right{width:224px}
.reason{position:relative;display:flex;align-items:center;background:linear-gradient(90deg,#0c0400 0%,#2a1000 18%,#b45200 55%,var(--orange) 80%,#ffb800 100%);box-shadow:inset 0 1px 0 rgba(255,220,120,.55),inset 0 -4px 6px rgba(0,0,0,.35);font-size:13px;line-height:14px;text-transform:uppercase;letter-spacing:-.2px;color:var(--white);text-shadow:0 1px 2px rgba(0,0,0,.7);padding-left:48px}
.reason--dot::before{content:"";position:absolute;left:28px;top:50%;width:11px;height:11px;margin-top:-5.5px;border-radius:50%;background:var(--white)}
.reasons__col--right .reason{padding-left:30px}
.reasons__col--right .reason--dot::before{left:10px}

.reasons-caption{left:0;width:468px;text-align:center;font-family:"Oswald",sans-serif;font-weight:500;color:#ffd800}
.reasons-caption__small{font-size:13px;line-height:16px}
.reasons-caption__big{font-size:28px;line-height:30px}

.call-band{left:0;width:468px;top:625px;height:87px;display:flex;flex-direction:column;justify-content:center;align-items:center;font-family:"Anton",sans-serif;font-size:33px;line-height:36px;letter-spacing:.8px}
.call-band--silver{background:linear-gradient(90deg,#6e6e6e 0%,#d8d8d8 15%,#f4f4f4 50%,#d8d8d8 85%,#6e6e6e 100%);color:#0a0a0a}
.call-band--red{background:var(--red);color:var(--white)}

/* contact */
.contact-photo{left:30px;top:716px;width:408px;height:120px;background:radial-gradient(ellipse at 50% 40%,#3a2c18 0%,#1a140c 45%,#050505 80%)}
.contact-icons{left:70px;top:732px;width:58px;text-align:center;color:var(--gold)}
.contact-icons svg{display:block;margin:0 auto}
.sms-label{font-family:"Montserrat",sans-serif;font-weight:500;font-size:20px;margin-top:20px}
.contact-divider{left:140px;top:718px;width:2px;height:110px;background:linear-gradient(180deg,transparent,#8a8a8a,transparent)}
.contact-numbers{left:166px;top:728px;font-family:"Montserrat",sans-serif;font-weight:500;font-size:38px;line-height:50px;letter-spacing:.5px;color:var(--white)}

.brand{left:0;width:468px;top:860px;display:flex;justify-content:center;align-items:center;gap:12px}
.brand__dot{width:28px;height:28px;border-radius:50%;background:var(--gold)}
.brand__name{font-family:"Montserrat",sans-serif;font-weight:600;font-size:26px;color:var(--gold);letter-spacing:.5px}
.web-address{left:0;width:468px;top:946px;text-align:center;font-family:"Montserrat",sans-serif;font-weight:500;font-size:12.5px;color:var(--white)}

/* back headline */
.back-title{left:0;width:468px;top:46px;text-align:center;font-family:"Montserrat",sans-serif;font-weight:600;font-size:24px;line-height:24px;letter-spacing:.5px}
.back-heat{left:0;width:468px;top:126px;text-align:center;font-family:"Anton",sans-serif;font-size:66px;line-height:72px;letter-spacing:-.5px}
.back-claims{left:58px;top:198px;width:362px;display:flex;align-items:center;justify-content:space-between}
.back-claims .privacy-claim__small{font-size:22px;letter-spacing:5px;line-height:24px}
.back-claims .privacy-claim__big{font-size:36px;line-height:38px}
.back-claims__divider{width:2px;height:52px;background:#aaa}
.back-money{left:0;width:468px;top:256px;text-align:center;font-size:80px}
.flyer--back .reason{padding-left:47px}
.flyer--back .reasons__col--right .reason{padding-left:30px}
</style>
</head>
<body>

<div class="side-label side-label--front">FRONTSIDE</div>
<div class="side-label side-label--back">BACKSIDE</div>

<!-- FRONT -->
<section class="flyer flyer--front">
  <div class="abs headline-stack gold-text">KEEP<br>HEAT<br>OUT</div>

  <div class="abs promo-tag promo-tag--uv">
    <div class="uv-claim"><div class="uv-claim__words">BLOCK<br>UV RAYS</div><div class="uv-claim__figure">99.9<sup>%</sup></div></div>
  </div>
  <div class="abs promo-tag promo-tag--privacy">
    <div class="privacy-claim"><div class="privacy-claim__small">INCREASE</div><div class="privacy-claim__big">PRIVATE</div></div>
  </div>

  <div class="abs save-money silver-text" style="left:34px;top:266px">SAVE MONEY</div>

  <div class="abs reasons" style="top:349px">
    <div class="reasons__col reasons__col--left">
      <div class="reason reason--dot" style="height:23px">Reduce glare</div>
      <div class="reason reason--dot" style="height:23px">Reduce energy costs</div>
      <div class="reason reason--dot" style="height:48px">Control the amount of<br>light entering your home</div>
      <div class="reason reason--dot" style="height:23px">Reduce carbon footprint</div>
      <div class="reason reason--dot" style="height:23px">Make home more beautiful</div>
      <div class="reason reason--dot" style="height:23px">Eliminate home hot spots.</div>
      <div class="reason reason--dot" style="height:23px">Protect against broken glass</div>
      <div class="reason reason--dot" style="height:23px">Regulate energy</div>
    </div>
    <div class="reasons__col reasons__col--right">
      <div class="reason reason--dot" style="height:23px">Protects upholstery</div>
      <div class="reason reason--dot" style="height:48px">Improve effectiveness<br>of roof insulation</div>
      <div class="reason reason--dot" style="height:23px">Improve health</div>
      <div class="reason reason--dot" style="height:23px">Reduces interior floor fading</div>
      <div class="reason reason--dot" style="height:23px">Eliminate need for blinds</div>
      <div class="reason reason--dot" style="height:23px">Strengthen your windows</div>
      <div class="reason reason--dot" style="height:23px">Insulate in winter</div>
      <div class="reason reason--dot" style="height:23px">Affordable</div>
    </div>
  </div>

  <div class="abs reasons-caption" style="top:576px">
    <div class="reasons-caption__small">20 REASONS WHY HOME WINDOW TINTING</div>
    <div class="reasons-caption__big">IS PERFECT FOR YOU</div>
  </div>

  <div class="abs call-band call-band--silver"><div>CALL BRISBANE’S LEADER IN</div><div>HOME WINDOW TINTING NOW</div></div>

  <div class="abs contact-photo" role="img" aria-label="Dark photo of a tinted car front"></div>
  <div class="abs contact-icons">
    <svg width="42" height="42" viewBox="0 0 42 42"><circle cx="21" cy="21" r="18" fill="none" stroke="currentColor" stroke-width="3"/><path d="M14 12c2-1 3 0 4 3 1 2 0 3-1 4 1 3 3 5 6 6 1-1 2-2 4-1 3 1 4 2 3 4-1 3-4 4-7 2-5-2-9-6-11-11-1-3 0-6 2-7z" fill="currentColor"/></svg>
    <div class="sms-label">SMS</div>
  </div>
  <div class="abs contact-divider"></div>
  <div class="abs contact-numbers">07 3000 4815<br>0400 555 192</div>

  <div class="abs brand"><span class="brand__dot"></span><span class="brand__name">BrightSun Window Tinting</span></div>
  <div class="abs web-address">www.brightsuntinting.com.au</div>
</section>

<!-- BACK -->
<section class="flyer flyer--back">
  <div class="abs back-title">20 REASONS WHY<br>HOME WINDOW TINTING<br>IS PERFECT FOR YOU</div>
  <div class="abs back-heat gold-text">KEEP HEAT OUT</div>
  <div class="abs back-claims">
    <div class="uv-claim"><div class="uv-claim__words">BLOCK<br>UV RAYS</div><div class="uv-claim__figure">99.9<sup>%</sup></div></div>
    <div class="back-claims__divider"></div>
    <div class="privacy-claim"><div class="privacy-claim__small">INCREASE</div><div class="privacy-claim__big">PRIVATE</div></div>
  </div>
  <div class="abs save-money back-money silver-text">SAVE MONEY</div>

  <div class="abs reasons" style="top:350px">
    <div class="reasons__col reasons__col--left">
      <div class="reason" style="height:26px">Reduce glare</div>
      <div class="reason" style="height:26px">Reduce energy costs</div>
      <div class="reason" style="height:52px">Control the amount of<br>light entering your home</div>
      <div class="reason" style="height:26px">Reduce carbon footprint</div>
      <div class="reason" style="height:26px">Make home more beautiful</div>
      <div class="reason" style="height:26px">Eliminate home hot spots.</div>
      <div class="reason" style="height:26px">Protect against broken glass</div>
      <div class="reason" style="height:26px">Regulate energy</div>
    </div>
    <div class="reasons__col reasons__col--right">
      <div class="reason reason--dot" style="height:26px">Protects upholstery</div>
      <div class="reason reason--dot" style="height:52px">Improve effectiveness<br>of roof insulation</div>
      <div class="reason reason--dot" style="height:26px">Improve health</div>
      <div class="reason reason--dot" style="height:26px">Reduces interior floor fading</div>
      <div class="reason reason--dot" style="height:26px">Eliminate need for blinds</div>
      <div class="reason reason--dot" style="height:26px">Strengthen your windows</div>
      <div class="reason reason--dot" style="height:26px">Insulate in winter</div>
      <div class="reason reason--dot" style="height:26px">Affordable</div>
    </div>
  </div>

  <div class="abs call-band call-band--red"><div>CALL BRISBANE’S LEADER IN</div><div>HOME WINDOW TINTING NOW</div></div>

  <div class="abs contact-photo" role="img" aria-label="Dark photo of a tinted car front"></div>
  <div class="abs contact-icons">
    <svg width="42" height="42" viewBox="0 0 42 42"><circle cx="21" cy="21" r="18" fill="none" stroke="currentColor" stroke-width="3"/><path d="M14 12c2-1 3 0 4 3 1 2 0 3-1 4 1 3 3 5 6 6 1-1 2-2 4-1 3 1 4 2 3 4-1 3-4 4-7 2-5-2-9-6-11-11-1-3 0-6 2-7z" fill="currentColor"/></svg>
    <div class="sms-label">SMS</div>
  </div>
  <div class="abs contact-divider"></div>
  <div class="abs contact-numbers">07 3000 4815<br>0400 555 192</div>

  <div class="abs brand"><span class="brand__dot"></span><span class="brand__name">BrightSun Window Tinting</span></div>
  <div class="abs web-address">www.brightsuntinting.com.au</div>
</section>

</body>
</html>
```